Analytics software company needs a business card design

We need a business card design for a global analytics software provider called 'Varnel Software'. Our main focus is developing real estate analysis software. We are open to any color scheme. The final design should be simple, modern, and precise.
Updates

There is one day left in our project and we are still looking forward to receiving additional submissions. We look forward to selecting one of your designs. Thanks.

Industry/Entity Type

Real Estate

```html
<!DOCTYPE html>
<html lang="en">
<head>
<meta charset="utf-8">
<title>Varnel Software – Business Card</title>
<link rel="stylesheet" href="https://fonts.googleapis.com/css2?family=Eagle+Lake&family=Mulish:ital,wght@1,400;1,700&display=swap">
<style>
  :root {
    --page-bg: #ffffff;
    --front-bg: #71706f;
    --band-black: #080808;
    --back-bg: #1e1d1d;
    --ink-dark: #111111;
    --ink-light: #ffffff;
    --gold: #c9a100;
    --silhouette: #1b1b1b;
    --skin-light: #e6c3ad;
    --skin-dark: #b98a72;
  }
  * { margin: 0; padding: 0; box-sizing: border-box; }
  html, body { width: 1200px; height: 1000px; overflow: hidden; background: var(--page-bg); }
  .canvas { position: relative; width: 1200px; height: 1000px; }

  .card { position: absolute; width: 640px; height: 350px; overflow: hidden; }
  .card--front { left: 145px; top: 100px; background: var(--front-bg); }
  .card--back { left: 415px; top: 545px; background: var(--back-bg); }

  .brand-name {
    position: absolute; left: 88px; top: 42px;
    font-family: "Eagle Lake", serif; font-size: 31px; font-weight: 400;
    line-height: 40px; letter-spacing: 0.3px; white-space: nowrap;
  }
  .card--front .brand-name { color: var(--ink-dark); }
  .card--back .brand-name { left: 100px; top: 42px; color: var(--ink-light); }

  .tagline {
    position: absolute; left: 72px; top: 106px;
    font-family: "Eagle Lake", serif; font-size: 15px; line-height: 20px;
    color: var(--gold); white-space: nowrap;
  }
  .card--back .tagline { left: 83px; top: 104px; }

  .side-band { position: absolute; right: 0; top: 0; width: 80px; height: 100%; background: var(--band-black); }

  .contact {
    position: absolute; left: 345px; top: 188px; list-style: none;
    font-family: "Mulish", sans-serif; font-style: italic; font-size: 18px;
    color: var(--ink-dark); line-height: 27px;
  }
  .contact .person-name { font-weight: 700; }

  .illustration-team {
    position: absolute; left: 0; top: 225px; width: 160px; height: 125px;
    background: linear-gradient(180deg, rgba(27,27,27,0.25), var(--silhouette));
  }
  .photo-hand {
    position: absolute; right: 0; bottom: 0; width: 230px; height: 220px;
    background: radial-gradient(circle at 60% 60%, var(--skin-light), var(--skin-dark) 70%, var(--back-bg) 100%);
  }
</style>
</head>
<body>
<main class="canvas">
  <section class="card card--front">
    <h1 class="brand-name">Varnel Software</h1>
    <p class="tagline">Global Analytic Software Provider</p>
    <div class="illustration-team" role="img" aria-label="Silhouettes of business people shaking hands and meeting at a table"></div>
    <ul class="contact">
      <li class="person-name">Name</li>
      <li>Designation</li>
      <li>Address</li>
      <li>90000000000</li>
      <li>hello@varnel.example</li>
    </ul>
    <div class="side-band"></div>
  </section>

  <section class="card card--back">
    <h2 class="brand-name">Varnel Software</h2>
    <p class="tagline">Global Analytic Software Provider</p>
    <div class="photo-hand" role="img" aria-label="Photo of a hand holding a black marker pen"></div>
  </section>
</main>
</body>
</html>
```